Business card for Chiropractic clinics needs reworked / redesigned

The business card in attachment was designed 10 years ago. It is in need of an update.
We have 2 clinics:
VELDHOVE KLINIEK & VELDHOVE KLINIEK NOORD
Only one address needs to be on the card for doctors that only work in one clinic and two addresses need to be on the card for the doctors that work in both clinics.

Target Market(s)

patients/referrers

Industry/Entity Type

Medical

Contact Information for Business Card

Logo (in full or zoomed-in)
Clinic Name
Doctor name and title
clinic address, website, tel, email

Font styles to use
Sans Serif

Colors

Designer to choose colors to be used in the design.

Requirements
Must have
• Good contrast/readability
• We like modern minimalistic designs
• The Bcard needs to project our very high standard of proficiency/professionalism
Should not have
• Not curly
• Not to much colours

```html
<!DOCTYPE html>
<html lang="en">
<head>
<meta charset="utf-8">
<title>Veldhove Kliniek – Business Card</title>
<link rel="stylesheet" href="https://fonts.googleapis.com/css2?family=Roboto:wght@400;700&family=Roboto+Condensed:wght@400;500&display=swap">
<style>
  :root {
    --backdrop: #d9d6d1;
    --paper: #fbfbfa;
    --ink-dark: #123130;
    --ink-text: #4a4f4f;
    --ink-muted: #6b7070;
    --white: #ffffff;
  }
  * { box-sizing: border-box; margin: 0; padding: 0; }
  html, body {
    width: 1200px;
    height: 911px;
    overflow: hidden;
    background: var(--backdrop);
  }
  .canvas {
    position: relative;
    width: 1200px;
    height: 911px;
    display: flex;
    align-items: center;
    justify-content: center;
    gap: 70px;
  }
  .card {
    position: relative;
    box-shadow: 0 10px 30px rgba(0,0,0,0.18);
    overflow: hidden;
  }

  /* Front: contact side */
  .card--front {
    width: 560px;
    height: 327px;
    background: var(--paper);
  }
  .contact {
    position: absolute;
    top: 40px;
    left: 300px;
    font-family: "Roboto", sans-serif;
    font-size: 13px;
    line-height: 1.45;
    color: var(--ink-text);
  }
  .contact__clinic { font-weight: 700; color: var(--ink-text); }
  .contact__address { margin-bottom: 6px; }
  .contact__list { list-style: none; margin-top: 4px; }
  .contact__list li { display: flex; align-items: center; gap: 8px; }
  .contact__list svg { width: 11px; height: 11px; flex: none; }
  .front-brand {
    position: absolute;
    left: 40px;
    top: 120px;
    display: flex;
    align-items: center;
    gap: 10px;
    font-family: "Roboto Condensed", sans-serif;
    font-weight: 500;
    font-size: 20px;
    letter-spacing: 0.04em;
    color: var(--ink-dark);
  }
  .front-brand__mark {
    width: 12px; height: 12px;
    background: var(--ink-dark);
  }
  .name-band {
    position: absolute;
    left: 0;
    bottom: 0;
    width: 280px;
    height: 82px;
    background: var(--ink-dark);
    color: var(--white);
    padding: 16px 0 0 24px;
    font-family: "Roboto Condensed", sans-serif;
  }
  .name-band__name {
    font-size: 19px;
    font-weight: 500;
    letter-spacing: 0.02em;
    text-transform: uppercase;
    white-space: nowrap;
  }
  .name-band__title {
    font-size: 14px;
    letter-spacing: 0.05em;
    text-transform: uppercase;
    margin-top: 2px;
  }

  /* Back: brand side */
  .card--back {
    width: 327px;
    height: 560px;
    background: var(--ink-dark);
  }
  .back-brand {
    position: absolute;
    left: 60px;
    bottom: 150px;
    display: flex;
    align-items: center;
    gap: 12px;
    font-family: "Roboto Condensed", sans-serif;
    font-weight: 500;
    font-size: 30px;
    line-height: 1.05;
    letter-spacing: 0.04em;
    color: var(--white);
  }
  .back-brand__mark {
    width: 16px; height: 16px;
    border-radius: 50%;
    background: var(--white);
    flex: none;
  }
</style>
</head>
<body>
<main class="canvas">

  <section class="card card--front" aria-label="Business card front">
    <div class="contact">
      <p class="contact__clinic">Veldhove Kliniek</p>
      <p class="contact__address">Lindenlaan 148, 9000 Veldhove</p>
      <p class="contact__clinic">Veldhove Kliniek Noord</p>
      <p class="contact__address">Kerkstraat 27</p>
      <ul class="contact__list">
        <li>
          <svg viewBox="0 0 12 12" aria-hidden="true"><path d="M2.5 1 L4.5 1 L5.2 3.6 L4 4.6 Q5 7 7.4 8 L8.4 6.8 L11 7.5 L11 9.5 Q10.5 11 9 11 Q1 10 1 3 Q1 1.5 2.5 1Z" fill="var(--ink-dark)"/></svg>
          <span>+32 (0)9 555 01 42</span>
        </li>
        <li>
          <svg viewBox="0 0 12 12" aria-hidden="true"><rect x="3" y="0.5" width="6" height="11" rx="1" fill="none" stroke="var(--ink-dark)" stroke-width="1.3"/><circle cx="6" cy="9.6" r="0.7" fill="var(--ink-dark)"/></svg>
          <span>0911 55 01 420</span>
        </li>
        <li>
          <svg viewBox="0 0 12 12" aria-hidden="true"><rect x="0.5" y="0.5" width="11" height="11" rx="2" fill="var(--ink-dark)"/><path d="M2.5 4 L6 6.5 L9.5 4 M2.5 4 V8.5 H9.5 V4" fill="none" stroke="var(--white)" stroke-width="1"/></svg>
          <span>info@veldhovekliniek.be</span>
        </li>
        <li>
          <svg viewBox="0 0 12 12" aria-hidden="true"><circle cx="6" cy="6" r="5.5" fill="var(--ink-dark)"/><path d="M0.8 6 H11.2 M6 0.6 Q3 6 6 11.4 M6 0.6 Q9 6 6 11.4" fill="none" stroke="var(--white)" stroke-width="0.8"/></svg>
          <span>www.veldhovekliniek.be</span>
        </li>
      </ul>
    </div>

    <div class="front-brand">
      <span class="front-brand__mark" aria-hidden="true"></span>
      <span>VELDHOVE KLINIEK</span>
    </div>

    <div class="name-band">
      <p class="name-band__name">Pieter Vandermeersch D.C.</p>
      <p class="name-band__title">Chiropractor</p>
    </div>
  </section>

  <section class="card card--back" aria-label="Business card back">
    <div class="back-brand">
      <span class="back-brand__mark" aria-hidden="true"></span>
      <span>VELDHOVE<br>KLINIEK</span>
    </div>
  </section>

</main>
</body>
</html>
```